Documentary Movie Needs a Poster

We need a poster/lobby card for a documentary film made by six filmmakers. Lobby card needs to list name of sponsor, names of filmmakers and (if feasible, but not required) image frames from each of the six sections of the film.

Text should be very readable. OK to have all caps text or upper/lower.

Design comps are OK, these do not need to be print-ready final images.

Target Market(s)

well educated documentary filmgoers

Industry/Entity Type

Movie

Requirements
Must have
• Must contain the following text (please use helvetica neue or similar font).

Please use the following sponsor name:

The
Marlowe Institute for Cinema
presents

Please use the following filmmaker names:

Theodore Pelusky
Robert Nash
Frederick Tamworth
Harold E. F. Pratt
Vincent Lorimer
Danny Frost

Please use the 6 images in archive/zip to create the card.

You can also do text-only versions of the card (no images).

Card needs to be 2:1 aspect ratio (2000px wide x 1000 pixels high)

Names of filmmakers should each be same size (no filmmaker has visual priority over the other).

Colors for text, lines and other design elements should be RED, BLACK and/or WHITE.

Feel free to crop images if you need to.

```html
<!DOCTYPE html>
<html lang="en">
<head>
<meta charset="utf-8">
<title>The Marlowe Institute for Cinema Presents</title>
<link rel="stylesheet" href="https://fonts.googleapis.com/css2?family=Inter+Tight:wght@600;700;800&display=swap">
<style>
  :root {
    --ink: #000000;
    --paper: #ffffff;
    --accent: #9a8738;
    --sky: #c9d3dc;
    --sand: #c9b594;
    --dust: #b9a98a;
    --stone: #a89677;
    --smoke: #8a8172;
  }
  * { margin: 0; padding: 0; box-sizing: border-box; }
  html, body { width: 1200px; height: 600px; overflow: hidden; background: var(--ink); }
  .lobby-card {
    position: relative;
    width: 1200px;
    height: 600px;
    background: var(--ink);
    color: var(--paper);
    font-family: "Inter Tight", "Helvetica Neue", Arial, sans-serif;
    font-weight: 700;
    text-transform: uppercase;
  }
  .sponsor {
    position: absolute;
    right: 828px;
    top: 56px;
    text-align: right;
    line-height: 1;
  }
  .sponsor__lead { font-size: 46px; font-weight: 800; letter-spacing: 0.5px; }
  .sponsor__name { font-size: 36px; font-weight: 800; letter-spacing: 7px; margin-top: 10px; margin-right: -7px; }
  .sponsor__tail { font-size: 23px; margin-top: 8px; }
  .sponsor__presents { font-size: 23px; margin-top: 8px; }
  .divider-vertical {
    position: absolute; left: 384px; top: 62px;
    width: 6px; height: 244px; background: var(--paper);
  }
  .filmmakers {
    position: absolute; left: 407px; top: 212px;
    list-style: none; font-size: 27px; line-height: 35.5px;
  }
  .filmmakers__row { display: flex; align-items: center; white-space: nowrap; }
  .filmmakers__sep {
    display: inline-block; width: 9px; height: 9px; border-radius: 50%;
    background: var(--accent); margin: 0 12px;
  }
  .divider-horizontal {
    position: absolute; left: 868px; top: 305px;
    width: 303px; height: 6px; background: var(--paper);
  }
  .frames {
    position: absolute; left: 30px; top: 368px;
    width: 1142px; height: 104px; display: flex;
  }
  .frame { height: 100%; }
  .frame--capitol { width: 197px; background: linear-gradient(180deg, var(--sky) 0%, #d8d4c8 55%, #4a4038 100%); }
  .frame--trench { width: 198px; background: linear-gradient(160deg, #d9d2c4 0%, #a9a08e 100%); }
  .frame--road { width: 210px; background: linear-gradient(180deg, #e6e4de 0%, var(--stone) 60%, #7d7260 100%); }
  .frame--rooftops { width: 213px; background: linear-gradient(180deg, #e2ddd2 0%, var(--sand) 50%, #8f7a58 100%); }
  .frame--crowd { width: 200px; background: linear-gradient(180deg, #d6d3cc 0%, var(--smoke) 55%, #4e4b45 100%); }
  .frame--wreck { width: 124px; background: linear-gradient(180deg, #ebe7df 0%, var(--dust) 100%); }
</style>
</head>
<body>
  <main class="lobby-card">
    <header class="sponsor">
      <p class="sponsor__lead">The Marlowe</p>
      <p class="sponsor__name">Institute</p>
      <p class="sponsor__tail">for Cinema</p>
      <p class="sponsor__presents">Presents</p>
    </header>

    <div class="divider-vertical"></div>

    <ul class="filmmakers">
      <li class="filmmakers__row">Theodore Pelusky<span class="filmmakers__sep"></span>Robert Nash</li>
      <li class="filmmakers__row">Frederick Tamworth<span class="filmmakers__sep"></span>Harold E. F. Pratt</li>
      <li class="filmmakers__row">Vincent Lorimer<span class="filmmakers__sep"></span>Danny Frost</li>
    </ul>

    <div class="divider-horizontal"></div>

    <section class="frames">
      <div class="frame frame--capitol" role="img" aria-label="Film still: protesters with signs in front of a domed government building"></div>
      <div class="frame frame--trench" role="img" aria-label="Film still: black and white photo of a soldier resting in a trench"></div>
      <div class="frame frame--road" role="img" aria-label="Film still: soldier kneeling on a desert road with troops behind"></div>
      <div class="frame frame--rooftops" role="img" aria-label="Film still: soldiers on rooftops overlooking a city with smoke rising"></div>
      <div class="frame frame--crowd" role="img" aria-label="Film still: crowd of armed men raising rifles"></div>
      <div class="frame frame--wreck" role="img" aria-label="Film still: wrecked military vehicle"></div>
    </section>
  </main>
</body>
</html>
```